online jewellery store business card

all black business card, glossy, with gold writing, gold logo and name (provided). simple design.

Target Market(s)

This business card is to put with purchases, so it just needs the logo and name Velmora Jewellery which I have uploaded pictures for you to use. Then it needs the web address, bidlorn address, email address and then the like us on KL for 10% off. All words to be used have been provided. Thanks

Industry/Entity Type

Store

Contact Information for Business Card

www.velmorajewellery.com
stores.bidlorn.com.au/Velmora-Jewellery
info@velmorajewellery.com

Like us on kinloop for 10% off your next purchase!

Requirements
Must have
• black background
gold writing
glossy look
Should not have
• yellow writing

```html
<!DOCTYPE html>
<html lang="en">
<head>
<meta charset="UTF-8">
<title>Velmora Jewellery – Business Card</title>
<link rel="stylesheet" href="https://fonts.googleapis.com/css2?family=Raleway:wght@300;400&display=swap">
<style>
  :root {
    --card-black: #0d0d0d;
    --card-charcoal: #1f1f1f;
    --gold: #c9a45c;
    --gold-muted: #a88748;
    --gold-line: #8c7443;
  }
  html, body {
    margin: 0;
    padding: 0;
    width: 1200px;
    height: 686px;
    overflow: hidden;
    background: var(--card-black);
  }
  .card {
    position: relative;
    width: 1200px;
    height: 686px;
    background:
      radial-gradient(ellipse 70% 60% at 50% 35%, var(--card-charcoal) 0%, var(--card-black) 100%);
    font-family: "Raleway", sans-serif;
    color: var(--gold);
  }
  .brand-mark {
    position: absolute;
    left: 50%;
    top: 139px;
    width: 206px;
    height: 206px;
    margin-left: -103px;
  }
  .brand-name {
    position: absolute;
    left: 0;
    right: 0;
    top: 352px;
    margin: 0;
    text-align: center;
    font-weight: 400;
    font-size: 48px;
    line-height: 66px;
    letter-spacing: 0.14em;
    padding-left: 0.14em;
    color: var(--gold);
  }
  .brand-name span { display: block; }
  .contact-details {
    position: absolute;
    left: 0;
    right: 0;
    top: 518px;
    margin: 0;
    text-align: center;
    font-weight: 400;
    font-size: 15px;
    line-height: 28px;
    letter-spacing: 0.12em;
    color: var(--gold-muted);
  }
  .contact-details span { display: block; }
  .contact-details .offer { color: var(--gold); }
  .web-address {
    position: absolute;
    left: 0;
    right: 0;
    top: 624px;
    margin: 0;
    text-align: center;
    font-weight: 400;
    font-size: 20px;
    letter-spacing: 29px;
    padding-left: 29px;
    color: var(--gold-muted);
  }
</style>
</head>
<body>
  <main class="card">
    <svg class="brand-mark" viewBox="0 0 206 206" aria-hidden="true">
      <circle cx="103" cy="103" r="96" fill="none" stroke="var(--gold-line)" stroke-width="2"/>
    </svg>
    <h1 class="brand-name">
      <span>VELMORA</span>
      <span>JEWELLERY</span>
    </h1>
    <p class="contact-details">
      <span>stores.bidlorn.com.au/Velmora-Jewellery &nbsp;·&nbsp; info@velmorajewellery.com</span>
      <span class="offer">Like us on kinloop for 10% off your next purchase!</span>
    </p>
    <p class="web-address">WWW.VELMORAJEWELLERY.COM</p>
  </main>
</body>
</html>
```